Ferris Contracting LLC Business Card Design

I am looking for a creative and unique business card design. We are a commercial construction general contractor. With the name "FERRIS" Contracting, I am hoping to see some neat designs that correlate with the name.

```html
<!DOCTYPE html>
<html lang="en">
<head>
<meta charset="UTF-8">
<title>Ferris Contracting LLC – Business Card</title>
<link href="https://fonts.googleapis.com/css2?family=Montserrat:wght@400;500;800&display=swap" rel="stylesheet">
<style>
  :root {
    --bg: #2b2b2d;
    --card-black: #141416;
    --card-white: #ffffff;
    --brand-blue: #2d8fd5;
    --brand-grey: #b9bcc0;
    --text-light: #f2f2f2;
  }
  * { box-sizing: border-box; margin: 0; padding: 0; }
  html, body { width: 1200px; height: 874px; overflow: hidden; }
  body {
    background: var(--bg);
    font-family: "Montserrat", sans-serif;
    position: relative;
  }
  .card {
    position: absolute;
    left: 270px;
    width: 660px;
    height: 377px;
    border-radius: 22px;
    overflow: hidden;
    box-shadow: 0 14px 30px rgba(0,0,0,0.45);
  }
  .card--front { top: 30px; background: var(--card-black); }
  .card--back { top: 452px; background: var(--card-black); }

  .brand {
    position: absolute;
    display: flex;
    align-items: center;
    gap: 14px;
    color: var(--brand-blue);
    font-weight: 800;
    text-transform: uppercase;
    white-space: nowrap;
  }
  .brand__name { display: flex; flex-direction: column; line-height: 1.05; }
  .brand__dot {
    border-radius: 50%;
    border: 6px solid var(--brand-grey);
    flex: none;
  }
  .card--front .brand {
    left: 50%; top: 50%;
    transform: translate(-50%, -50%);
    font-size: 46px;
    letter-spacing: 2px;
  }
  .card--front .brand__dot { width: 60px; height: 60px; }

  .back-art { position: absolute; inset: 0; }

  .card--back .brand {
    left: 372px; top: 62px;
    font-size: 28px;
    letter-spacing: 1px;
    gap: 12px;
  }
  .card--back .brand__dot { width: 38px; height: 38px; border-width: 4px; }

  .contact-block {
    position: absolute;
    left: 40px; top: 168px;
    color: var(--text-light);
  }
  .person__name {
    color: var(--brand-blue);
    font-weight: 800;
    font-size: 24px;
    letter-spacing: 0.5px;
  }
  .person__title { font-size: 17px; margin-top: 2px; }
  .contact-list { list-style: none; margin-top: 20px; font-size: 17px; line-height: 26px; }
  .contact-list li { display: flex; align-items: center; gap: 8px; }
  .contact-list svg { width: 14px; height: 14px; fill: var(--brand-blue); flex: none; }

  .address {
    position: absolute;
    right: 40px; bottom: 18px;
    text-align: right;
    color: var(--text-light);
    font-size: 18px;
    line-height: 28px;
  }
</style>
</head>
<body>

<section class="card card--front">
  <div class="brand">
    <span class="brand__dot"></span>
    <span class="brand__name"><span>Ferris</span><span>Contracting</span></span>
  </div>
</section>

<section class="card card--back">
  <svg class="back-art" viewBox="0 0 660 377" width="660" height="377" aria-hidden="true">
    <path d="M0,0 H660 V255 C570,285 480,265 430,205 C360,120 240,82 0,108 Z" fill="var(--card-white)"/>
    <path d="M0,96 C240,70 362,108 434,194 C484,254 574,273 660,243" fill="none" stroke="var(--brand-grey)" stroke-width="5"/>
    <path d="M0,108 C240,82 360,120 430,205 C480,265 570,285 660,255" fill="none" stroke="var(--brand-blue)" stroke-width="9"/>
    <path d="M120,94 C270,90 370,140 426,208 C478,270 570,292 660,264" fill="none" stroke="var(--brand-blue)" stroke-width="3" opacity="0.7"/>
  </svg>

  <div class="brand">
    <span class="brand__dot"></span>
    <span class="brand__name"><span>Ferris</span><span>Contracting</span></span>
  </div>

  <div class="contact-block">
    <p class="person__name">DANA WHITLOW</p>
    <p class="person__title">Managing Director</p>
    <ul class="contact-list">
      <li><svg viewBox="0 0 24 24"><path d="M6.6 10.8a15 15 0 0 0 6.6 6.6l2.2-2.2c.3-.3.7-.4 1-.2 1.1.4 2.3.6 3.6.6.6 0 1 .4 1 1V20c0 .6-.4 1-1 1A17 17 0 0 1 3 4c0-.6.4-1 1-1h3.5c.6 0 1 .4 1 1 0 1.3.2 2.5.6 3.6.1.3 0 .7-.2 1z"/></svg>555 018 274</li>
      <li><svg viewBox="0 0 24 24"><path d="M2 5h20v14H2z M2 5l10 8 10-8" /></svg>info@ferriscontracting.com</li>
      <li><svg viewBox="0 0 24 24"><circle cx="12" cy="12" r="10"/></svg>www.ferriscontracting.com</li>
    </ul>
  </div>

  <p class="address">Your address, City<br>State, Zip 1200</p>
</section>

</body>
</html>
```